Kestrel Bathrooms

Fix our flyer add as the one we got made has the wrong phone number on it would like different photos on it

Want it to Stand out and be in your face!

I will attach our logo
phone number is 0487265903
Email is Miles@kestrelbathrooms.com.au

happy to keep all prices the same

If you can make it better happy to tip $$

```html
<!DOCTYPE html>
<html lang="en">
<head>
<meta charset="utf-8">
<title>Kestrel Bathrooms – Flyer</title>
<link href="https://fonts.googleapis.com/css2?family=Libre+Franklin:wght@300;400;600;800;900&display=swap" rel="stylesheet">
<style>
  :root {
    --brand-blue: #2b3e91;
    --logo-blue: #1f5fae;
    --ink: #2a2a2a;
    --muted: #8c8c8c;
    --rule: #c9c9c9;
    --band: #d4d2d6;
    --paper: #ffffff;
  }
  * { box-sizing: border-box; margin: 0; padding: 0; }
  html, body { width: 903px; height: 1200px; overflow: hidden; background: #f2f2f2; }
  body { font-family: "Libre Franklin", Arial, sans-serif; color: var(--ink); }

  .flyer { position: relative; width: 903px; height: 1200px; background: var(--paper); overflow: hidden; }

  .site-url { position: absolute; top: 34px; left: 0; width: 903px; text-align: center;
    font-size: 14px; letter-spacing: 2.4px; color: var(--brand-blue); }

  .brand { position: absolute; left: 64px; top: 72px; }
  .brand-name { font-size: 44px; font-weight: 800; color: var(--logo-blue); letter-spacing: 1px; line-height: 1; }
  .brand-tagline { margin-top: 22px; margin-left: 100px; font-size: 19px; font-weight: 300; color: var(--muted); letter-spacing: .5px; }

  .seal { position: absolute; }
  .seal-local { left: 684px; top: 36px; }
  .seal-licensed { left: 337px; top: 994px; z-index: 2; }

  .rule { position: absolute; height: 1px; background: var(--rule); }
  .rule-top { left: 64px; width: 775px; top: 222px; }
  .rule-mid { left: 64px; width: 775px; top: 716px; }
  .rule-low-left { left: 64px; width: 300px; top: 1022px; }
  .rule-low-right { left: 516px; width: 330px; top: 1022px; }

  .hero { position: absolute; left: 0; top: 234px; width: 903px; height: 470px;
    background: linear-gradient(180deg, #8d8c8e 0%, #b9b4ad 35%, #d9cfc2 60%, #c7ad8c 85%, #b69a77 100%); }
  .hero-title { position: absolute; left: 64px; top: 262px; color: #fff; font-weight: 300;
    font-size: 42px; line-height: 1.08; letter-spacing: .5px; }

  .package { position: absolute; top: 730px; width: 248px; }
  .package-main { left: 55px; }
  .package-ensuite { left: 329px; }
  .package-laundry { left: 601px; }
  .package-photo { position: relative; height: 158px; }
  .photo-main { background: linear-gradient(135deg, #1f4a33, #3d6b4d 50%, #d9d3cf); }
  .photo-ensuite { background: linear-gradient(90deg, #2a2a2c 0%, #dfe3e6 40%, #e9e9ea 65%, #a4663a 100%); }
  .photo-laundry { background: linear-gradient(135deg, #7c6a62, #a5958b 50%, #e7dccd); }
  .package-save { position: absolute; left: 22px; bottom: 2px; color: #fff; font-size: 15px; font-weight: 400; }
  .package-save strong { font-weight: 800; }
  .package-save::before { content: ""; display: inline-block; width: 8px; height: 8px; border: 1.5px solid #fff;
    transform: rotate(45deg); margin-right: 8px; vertical-align: 2px; }
  .package-info { margin-top: 12px; border-left: 1px solid var(--brand-blue); padding-left: 16px; }
  .package-title { font-size: 21px; font-weight: 900; color: var(--brand-blue); line-height: .98; text-transform: uppercase; }
  .package-from { margin-top: 5px; font-size: 15px; font-weight: 400; }
  .package-price { font-size: 31px; font-weight: 900; color: var(--brand-blue); line-height: 1.05; }

  .contact-band { position: absolute; left: 0; top: 1033px; width: 903px; height: 167px; background: var(--band); }
  .contact { position: absolute; left: 56px; top: 1055px; width: 270px; text-align: center; }
  .contact-lead { font-size: 25px; font-weight: 400; letter-spacing: .3px; }
  .contact-phone { font-size: 28px; font-weight: 900; color: var(--brand-blue); line-height: 1.1; }
  .contact-email { margin-top: 4px; font-size: 16px; white-space: nowrap; }

  .services { position: absolute; left: 511px; top: 1050px; }
  .services-title { font-size: 20px; font-weight: 900; color: var(--brand-blue); }
  .services-list { list-style: none; display: grid; grid-template-columns: 127px 130px; row-gap: 1px; margin-top: 2px; }
  .services-list li { font-size: 15px; font-weight: 600; color: #262626; }
  .services-list li::before { content: ""; display: inline-block; width: 7px; height: 7px; border: 1.5px solid var(--brand-blue);
    transform: rotate(45deg); margin: 0 7px 0 2px; vertical-align: 2px; }

  .footnote { position: absolute; top: 1170px; font-size: 10px; color: #333; }
  .footnote-terms { left: 64px; }
  .footnote-fixtures { left: 560px; }
</style>
</head>
<body>
<main class="flyer">
  <p class="site-url">WWW.KESTRELBATHROOMS.COM.AU</p>

  <div class="brand">
    <p class="brand-name">KESTREL BATHROOMS</p>
    <p class="brand-tagline">Your local renovation specialist</p>
  </div>

  <svg class="seal seal-local" width="150" height="150" viewBox="0 0 150 150" aria-label="Illawarra based and family operated">
    <g transform="translate(75 75)">
      <g fill="#d4d2d6" stroke="#2b3e91" stroke-width="2.4">
        <rect x="-50" y="-50" width="100" height="100" rx="20"/>
        <rect x="-50" y="-50" width="100" height="100" rx="20" transform="rotate(15)"/>
        <rect x="-50" y="-50" width="100" height="100" rx="20" transform="rotate(30)"/>
        <rect x="-50" y="-50" width="100" height="100" rx="20" transform="rotate(45)"/>
        <rect x="-50" y="-50" width="100" height="100" rx="20" transform="rotate(60)"/>
        <rect x="-50" y="-50" width="100" height="100" rx="20" transform="rotate(75)"/>
      </g>
      <g fill="#d4d2d6">
        <rect x="-50" y="-50" width="100" height="100" rx="20"/>
        <rect x="-50" y="-50" width="100" height="100" rx="20" transform="rotate(15)"/>
        <rect x="-50" y="-50" width="100" height="100" rx="20" transform="rotate(30)"/>
        <rect x="-50" y="-50" width="100" height="100" rx="20" transform="rotate(45)"/>
        <rect x="-50" y="-50" width="100" height="100" rx="20" transform="rotate(60)"/>
        <rect x="-50" y="-50" width="100" height="100" rx="20" transform="rotate(75)"/>
      </g>
      <circle r="54" fill="none" stroke="#2b3e91" stroke-width="1.4"/>
      <g transform="rotate(20)" fill="#2b3e91" font-family="Libre Franklin, Arial, sans-serif" font-size="13" text-anchor="middle">
        <text y="-22">ILLAWARRA</text>
        <text y="-7">BASED &amp;</text>
        <text y="8">FAMILY</text>
        <text y="23">OPERATED</text>
      </g>
    </g>
  </svg>

  <div class="rule rule-top"></div>

  <div class="hero" role="img" aria-label="Photo of a luxury bathroom with timber vanity, double basins and a leafy plant"></div>
  <h1 class="hero-title">LUXURY BATHROOM<br>DESIGN &amp; INSTALLATION</h1>

  <div class="rule rule-mid"></div>

  <section class="package package-main">
    <div class="package-photo photo-main" role="img" aria-label="Photo of a main bathroom with green tiles and a white basin">
      <p class="package-save">SAVE UP TO <strong>$4,000</strong></p>
    </div>
    <div class="package-info">
      <h2 class="package-title">Main Bathroom<br>Package</h2>
      <p class="package-from">Price starts from</p>
      <p class="package-price">$18,900</p>
    </div>
  </section>

  <section class="package package-ensuite">
    <div class="package-photo photo-ensuite" role="img" aria-label="Photo of an ensuite with a freestanding bath by a bright window">
      <p class="package-save">SAVE UP TO <strong>$4,000</strong></p>
    </div>
    <div class="package-info">
      <h2 class="package-title">Ensuite<br>Package</h2>
      <p class="package-from">Price starts from</p>
      <p class="package-price">$14,900</p>
    </div>
  </section>

  <section class="package package-laundry">
    <div class="package-photo photo-laundry" role="img" aria-label="Photo of a laundry with a front-load washer under a stone benchtop">
      <p class="package-save">SAVE UP TO <strong>$4,000</strong></p>
    </div>
    <div class="package-info">
      <h2 class="package-title">Laundry<br>Package</h2>
      <p class="package-from">Price starts from</p>
      <p class="package-price">$9,900</p>
    </div>
  </section>

  <div class="rule rule-low-left"></div>
  <div class="rule rule-low-right"></div>

  <div class="contact-band"></div>

  <svg class="seal seal-licensed" width="150" height="150" viewBox="0 0 150 150" aria-label="Fully licensed and insured">
    <g transform="translate(75 75)">
      <g fill="#d4d2d6" stroke="#2b3e91" stroke-width="1.6">
        <rect x="-48" y="-48" width="96" height="96" rx="20"/>
        <rect x="-48" y="-48" width="96" height="96" rx="20" transform="rotate(15)"/>
        <rect x="-48" y="-48" width="96" height="96" rx="20" transform="rotate(30)"/>
        <rect x="-48" y="-48" width="96" height="96" rx="20" transform="rotate(45)"/>
        <rect x="-48" y="-48" width="96" height="96" rx="20" transform="rotate(60)"/>
        <rect x="-48" y="-48" width="96" height="96" rx="20" transform="rotate(75)"/>
      </g>
      <g fill="#d4d2d6">
        <rect x="-48" y="-48" width="96" height="96" rx="20"/>
        <rect x="-48" y="-48" width="96" height="96" rx="20" transform="rotate(15)"/>
        <rect x="-48" y="-48" width="96" height="96" rx="20" transform="rotate(30)"/>
        <rect x="-48" y="-48" width="96" height="96" rx="20" transform="rotate(45)"/>
        <rect x="-48" y="-48" width="96" height="96" rx="20" transform="rotate(60)"/>
        <rect x="-48" y="-48" width="96" height="96" rx="20" transform="rotate(75)"/>
      </g>
      <circle r="52" fill="none" stroke="#2b3e91" stroke-width="1"/>
      <g transform="rotate(-20)" fill="#2b3e91" font-family="Libre Franklin, Arial, sans-serif" font-size="13" text-anchor="middle">
        <text y="-12">FULLY</text>
        <text y="3">LICENSED &amp;</text>
        <text y="18">INSURED</text>
      </g>
    </g>
  </svg>

  <div class="contact">
    <p class="contact-lead">CALL US AT</p>
    <p class="contact-phone">0487 265 903</p>
    <p class="contact-email">miles@kestrelbathrooms.com.au</p>
  </div>

  <div class="services">
    <h2 class="services-title">BUILT TO LAST</h2>
    <ul class="services-list">
      <li>Demolition</li><li>Plumbing</li>
      <li>Electrical</li><li>Tiling</li>
      <li>Carpentry</li><li>Waterproofing</li>
      <li>Design</li><li>Consultation</li>
    </ul>
  </div>

  <p class="footnote footnote-terms">*Terms and conditions apply and onsite quote required.</p>
  <p class="footnote footnote-fixtures">Organisation and delivery of all fixtures.</p>
</main>
</body>
</html>
```